Hi,
Brackwell Construction is a domestic builder on the Gold Coast specializing in new homes, townhouses, duplexes and high end renovations.
Brackwell Construction can make your dream new home or development a reality. Whether you already have plans or require a complete design and construct project service, Brackwell Construction will make your project a stress free experience.
We offer design, town planning, certification and construction services.

Target Market(s)

Anyone looking to build.

Industry/Entity Type

Building

Coding

Coded - Design and coding required

Font styles to use
Other font styles liked:
• Match logo

Colors

Designer to choose colors to be used in the design.

Requirements
Must have
• Attractive home page with logo etc.
• About us page
• Gallery page
• Services Page
• Contact us page

```html
<!DOCTYPE html>
<html lang="en">
<head>
<meta charset="utf-8">
<title>Brackwell Construction</title>
<link rel="stylesheet" href="https://fonts.googleapis.com/css2?family=Poppins:wght@300;400;500;600&family=Open+Sans:wght@400;600&display=swap">
<style>
:root{
  --navy:#15185a;
  --navy-deep:#0d1040;
  --orange:#f7860f;
  --orange-dark:#e56d05;
  --ink:#1d1d1d;
  --text:#555;
  --light:#e9e9e9;
  --black:#0b0b0b;
  --white:#fff;
}
*{box-sizing:border-box;margin:0;padding:0}
html,body{width:1200px;height:4276px;overflow:hidden}
body{font-family:"Open Sans",sans-serif;color:var(--ink);background:var(--white);position:relative}
h1,h2,h3,h4,.nav,.btn{font-family:"Poppins",sans-serif}
section,header,footer{position:absolute;left:0;width:1200px}
.underline{display:block;width:110px;height:3px;background:var(--orange);margin:14px auto 0}
.btn{display:inline-block;background:var(--orange);color:var(--white);font-size:17px;border-radius:2px}

/* header */
.site-header{top:0;height:105px;background:var(--white)}
.brand-box{position:absolute;left:0;top:0;width:265px;height:105px;background:var(--navy-deep);display:flex;flex-direction:column;align-items:center;justify-content:center;color:var(--white)}
.brand-mark{width:44px;height:44px;border:2px solid var(--white);border-radius:50%}
.brand-name{font-family:"Poppins",sans-serif;font-size:15px;margin-top:4px;letter-spacing:.5px}
.nav{position:absolute;right:95px;top:40px;display:flex;gap:44px;font-size:17px;color:var(--ink)}
.nav .active{color:var(--orange)}
.search-icon{position:absolute;right:35px;top:38px}

/* hero */
.hero{top:105px;height:590px;background:linear-gradient(100deg,#8c8f93 0%,#b7b9bb 40%,#c9a54a 62%,#5b5f66 85%,#34363a 100%)}
.hero-text{position:absolute;left:85px;top:140px;color:var(--white)}
.hero-text h1{font-weight:500;font-size:78px;line-height:74px}
.hero-text p{font-family:"Poppins",sans-serif;font-size:33px;line-height:40px;margin-top:14px}
.hero-text .btn{margin-top:28px;padding:12px 22px;font-size:22px}
.hero-dots{position:absolute;right:34px;top:270px;display:flex;flex-direction:column;gap:12px}
.hero-dots i{display:block;width:9px;height:9px;border-radius:50%;background:rgba(255,255,255,.7)}

/* about */
.about{top:695px;height:575px}
.about-frame{position:absolute;left:85px;top:103px;width:445px;height:345px;background:var(--navy-deep)}
.about-media{position:absolute;left:108px;top:128px;width:445px;height:322px;background:linear-gradient(135deg,#a98d64,#c9b27a 45%,#7c6a4d);box-shadow:0 8px 22px rgba(0,0,0,.3)}
.play{position:absolute;left:193px;top:131px;width:62px;height:62px;border-radius:50%;background:rgba(40,40,40,.75)}
.about-copy{position:absolute;left:612px;top:135px;width:505px}
.about-copy h4{font-weight:400;font-size:27px}
.about-copy h2{font-weight:500;font-size:45px;line-height:52px}
.about-copy .rule{width:340px;height:3px;background:var(--navy-deep);margin:6px 0 22px}
.about-copy p{font-size:13px;line-height:28px;color:var(--text)}
.about-copy .btn{margin-top:22px;padding:7px 38px;font-size:16px}

/* specialties */
.specialties{top:1270px;height:495px;background:linear-gradient(90deg,#f37b10,#f8861d 50%,#f07511)}
.specialties h2{position:absolute;top:85px;width:100%;text-align:center;color:var(--white);font-weight:500;font-size:48px}
.specialties .underline{background:var(--white)}
.spec-list{position:absolute;top:230px;left:88px;display:flex;gap:22px}
.spec-card{width:240px;height:160px;background:var(--white);display:flex;flex-direction:column;align-items:center;justify-content:center;gap:14px;box-shadow:0 4px 10px rgba(0,0,0,.2)}
.spec-card h3{font-weight:500;font-size:20px}

/* offers */
.offers{top:1765px;height:680px}
.offers h2{position:absolute;top:130px;width:100%;text-align:center;font-weight:500;font-size:48px}
.offer-list{position:absolute;top:240px;left:85px;display:flex;gap:42px}
.offer{width:315px}
.offer-media{height:205px}
.offer h3{font-weight:500;font-size:23px;margin-top:20px}
.offer p{font-size:14px;line-height:24px;color:var(--text);margin-top:10px;width:300px}
.arrow{position:absolute;top:325px;width:34px;height:34px;border-radius:50%;background:var(--white);box-shadow:0 1px 5px rgba(0,0,0,.25);display:flex;align-items:center;justify-content:center}

/* cta */
.cta{top:2445px;height:415px;background:linear-gradient(90deg,var(--navy-deep),#1b2070 50%,var(--navy-deep));color:var(--white);text-align:center}
.cta h2{margin-top:88px;font-weight:500;font-size:44px}
.cta .underline{background:var(--white)}
.cta p{width:840px;margin:36px auto 0;font-size:13px;line-height:31px}
.cta .btn{margin-top:36px;padding:8px 22px;font-size:16px}

/* gallery */
.gallery{top:2860px;height:860px;text-align:center}
.gallery h2{margin-top:138px;font-weight:500;font-size:48px}
.gallery-grid{position:absolute;left:85px;top:255px;display:grid;grid-template-columns:repeat(4,248px);grid-auto-rows:200px;gap:10px 12px}
.view-more{position:absolute;top:730px;width:100%;font-family:"Poppins",sans-serif;font-size:21px;color:var(--orange)}

/* partners */
.partners{top:3720px;height:130px;background:var(--light);display:flex;align-items:center;justify-content:space-around;padding:0 60px}
.partner-badge{width:140px;height:26px;border-radius:4px;background:#b9b9b9}

/* footer */
.site-footer{top:3850px;height:426px;background:var(--black);color:var(--white)}
.footer-brand{position:absolute;left:105px;top:85px;width:130px;text-align:center}
.footer-brand .mark{width:100px;height:100px;border:2px solid var(--white);border-radius:50%;margin:0 auto}
.footer-brand .name{font-family:"Poppins",sans-serif;font-size:30px;font-weight:300;margin-top:8px;letter-spacing:1px}
.footer-col{position:absolute;top:75px}
.footer-col h4{font-weight:400;font-size:17px;margin-bottom:28px}
.contact-col{left:435px}
.contact-col li{display:flex;gap:18px;font-size:13px;line-height:19px;margin-bottom:20px;list-style:none}
.links-col{left:728px}
.links-col li{list-style:none;font-size:12px;line-height:22px}
.links-col li::before{content:"›";margin-right:10px}
.follow-col{left:948px}
.follow-col li{list-style:none;display:flex;align-items:center;gap:10px;font-size:14px;margin-bottom:14px}
.follow-col li i{width:26px;height:26px;border:1.5px solid var(--white);border-radius:50%;display:inline-block}
.footer-bottom{position:absolute;top:352px;width:100%;text-align:center;font-size:13px}
</style>
</head>
<body>

<header class="site-header">
  <div class="brand-box"><div class="brand-mark"></div><div class="brand-name">Brackwell</div></div>
  <nav class="nav"><span class="active">Home</span><span>About us</span><span>Gallery</span><span>Services</span><span>Contact us</span></nav>
  <svg class="search-icon" width="24" height="24" viewBox="0 0 24 24"><circle cx="10" cy="10" r="7" fill="none" stroke="#1d1d1d" stroke-width="3"/><line x1="15" y1="15" x2="21" y2="21" stroke="#1d1d1d" stroke-width="3.5" stroke-linecap="round"/></svg>
</header>

<section class="hero" role="img" aria-label="Builder in a hard hat and tool belt on a building site">
  <div class="hero-text">
    <h1>We Are Your<br>Trusted Builder</h1>
    <p>It is a long established fact that<br>a reader will be distracted</p>
    <span class="btn">View More</span>
  </div>
  <div class="hero-dots"><i></i><i></i><i></i><i></i></div>
</section>

<section class="about">
  <div class="about-frame"></div>
  <div class="about-media" role="img" aria-label="Video of a team of builders in safety vests">
    <div class="play"><svg width="62" height="62" viewBox="0 0 62 62"><polygon points="25,19 25,43 44,31" fill="#fff"/></svg></div>
  </div>
  <div class="about-copy">
    <h4>About</h4>
    <h2>Brackwell Constructions</h2>
    <div class="rule"></div>
    <p>The point of using Lorem Ipsum is that it has a more-or-less normal distribution of letters, as opposed to using 'Content here, content here', making it look like readable English. Many desktop publishing packages and web page editors now use Lorem Ipsum as their default model text, and a search for 'lorem ipsum' will uncover many web sites still in their infancy.</p>
    <span class="btn">Read More</span>
  </div>
</section>

<section class="specialties">
  <h2>Specializing in<span class="underline"></span></h2>
  <div class="spec-list">
    <div class="spec-card"><svg width="70" height="62" viewBox="0 0 70 62" fill="none" stroke="#f7860f" stroke-width="2.5"><path d="M5 30 L35 5 L65 30"/><path d="M13 24 V57 H57 V24"/><rect x="29" y="38" width="12" height="19"/><path d="M35 18 a5 5 0 1 1 0.1 0"/></svg><h3>New Homes</h3></div>
    <div class="spec-card"><svg width="70" height="62" viewBox="0 0 70 62" fill="none" stroke="#f7860f" stroke-width="2.5"><path d="M8 28 L35 6 L62 28"/><rect x="14" y="26" width="42" height="31"/><rect x="29" y="40" width="12" height="17"/><rect x="19" y="32" width="8" height="7"/><rect x="43" y="32" width="8" height="7"/></svg><h3>Townhouses</h3></div>
    <div class="spec-card"><svg width="70" height="62" viewBox="0 0 70 62" fill="none" stroke="#f7860f" stroke-width="2.5"><rect x="8" y="12" width="24" height="45"/><rect x="38" y="6" width="24" height="51"/><path d="M13 20h6M21 20h6M13 30h6M21 30h6M13 40h6M21 40h6M43 16h6M51 16h6M43 26h6M51 26h6M43 36h6M51 36h6M43 46h6M51 46h6"/></svg><h3>Duplexes</h3></div>
    <div class="spec-card"><svg width="70" height="62" viewBox="0 0 70 62" fill="none" stroke="#f7860f" stroke-width="2.5"><path d="M6 30 L35 6 L64 30"/><path d="M12 25 V57 H58 V25"/><path d="M24 48 L46 26 M40 26 h6 v6"/><rect x="20" y="34" width="10" height="10"/></svg><h3>High end Renovations</h3></div>
  </div>
</section>

<section class="offers">
  <h2>We Offer<span class="underline"></span></h2>
  <div class="arrow" style="left:34px"><svg width="12" height="14" viewBox="0 0 12 14"><path d="M8 2 L3 7 L8 12" fill="none" stroke="#555" stroke-width="1.8"/></svg></div>
  <div class="arrow" style="left:1120px"><svg width="12" height="14" viewBox="0 0 12 14"><path d="M4 2 L9 7 L4 12" fill="none" stroke="#555" stroke-width="1.8"/></svg></div>
  <div class="offer-list">
    <div class="offer"><div class="offer-media" role="img" aria-label="Aerial model of a planned town with colourful houses" style="background:linear-gradient(135deg,#d9c9a2,#c0553a 45%,#5d8f3e)"></div><h3>Town Planning</h3><p>It is a long established fact that a reader will be distracted by the readable content</p></div>
    <div class="offer"><div class="offer-media" role="img" aria-label="Two storey house under a blue sky" style="background:linear-gradient(180deg,#4d8fd6,#7f9cbd 45%,#5e6672)"></div><h3>Certification</h3><p>It is a long established fact that a reader will be distracted by the readable content</p></div>
    <div class="offer"><div class="offer-media" role="img" aria-label="Construction workers in hard hats on site" style="background:linear-gradient(135deg,#6b6f74,#c6a63a 50%,#3c3f44)"></div><h3>Construction Services</h3><p>It is a long established fact that a reader will be distracted by the readable content</p></div>
  </div>
</section>

<section class="cta">
  <h2>Ready To Work with Our Company?<span class="underline"></span></h2>
  <p>The point of using Lorem Ipsum is that it has a more-or-less normal distribution of letters, as opposed to using 'Content here, content here', making it look like readable English. Many desktop publishing packages and web page editors now use Lorem Ipsum as their default model text, and a search for 'lorem ipsum' will uncover many web sites still in their infancy.</p>
  <span class="btn">Get a Quote</span>
</section>

<section class="gallery">
  <h2>Our Gallery<span class="underline"></span></h2>
  <div class="gallery-grid">
    <div role="img" aria-label="Modern grey two storey home" style="background:linear-gradient(180deg,#8aa3bf,#4a4f57)"></div>
    <div role="img" aria-label="Navy weatherboard house with garden" style="background:linear-gradient(180deg,#6c8fb0,#34415a 60%,#5c7a3c)"></div>
    <div role="img" aria-label="Builder measuring timber" style="background:linear-gradient(135deg,#3b3f45,#b5a08a 60%,#e2dfdc)"></div>
    <div role="img" aria-label="Bright interior with timber staircase" style="background:linear-gradient(135deg,#f0ede8,#c7794a 60%,#e6e1da)"></div>
    <div role="img" aria-label="Plans and tools on a desk" style="background:linear-gradient(135deg,#f1f1f1,#d8d4cf 60%,#c23a2d)"></div>
    <div role="img" aria-label="Kitchen interior under renovation" style="background:linear-gradient(135deg,#5d554a,#b4a48a 50%,#3a342c)"></div>
    <div role="img" aria-label="Dark timber two storey home" style="background:linear-gradient(180deg,#9fb1c6,#2f3b36 55%,#5e7a3a)"></div>
    <div role="img" aria-label="Townhouses in brown tones" style="background:linear-gradient(180deg,#c7c2b6,#7a5f40 55%,#5a4c38)"></div>
  </div>
  <div class="view-more">View More »</div>
</section>

<section class="partners">
  <div class="partner-badge"></div><div class="partner-badge"></div><div class="partner-badge"></div><div class="partner-badge"></div><div class="partner-badge"></div>
</section>

<footer class="site-footer">
  <div class="footer-brand"><div class="mark"></div><div class="name">Brackwell</div></div>
  <div class="footer-col contact-col">
    <h4>CONTACT US</h4>
    <ul>
      <li><svg width="14" height="18" viewBox="0 0 14 18"><path d="M7 1a6 6 0 0 1 6 6c0 4-6 10-6 10S1 11 1 7a6 6 0 0 1 6-6z" fill="#fff"/><circle cx="7" cy="7" r="2.2" fill="#0b0b0b"/></svg><span>42 Ridge Street, Southport,<br>QLD 4215</span></li>
      <li><svg width="14" height="16" viewBox="0 0 14 16"><path d="M3 1l3 3-2 2c1 2 3 4 5 5l2-2 3 3-2 3C6 15-1 8 0 3z" fill="#fff"/></svg><span>07 5550 1842</span></li>
      <li><svg width="14" height="12" viewBox="0 0 14 12"><rect x="0" y="1" width="14" height="10" fill="#fff"/><path d="M0 1l7 6 7-6" fill="none" stroke="#0b0b0b" stroke-width="1.3"/></svg><span>info@brackwellbuild.com</span></li>
    </ul>
  </div>
  <div class="footer-col links-col">
    <h4>QUICK LINKS</h4>
    <ul><li>Home</li><li>About us</li><li>Product</li><li>Services</li><li>Contact Us</li></ul>
  </div>
  <div class="footer-col follow-col">
    <h4>FOLLOW US</h4>
    <ul><li><i></i>Newsfeed</li><li><i></i>Updates</li><li><i></i>Circles</li><li><i></i>Videos</li></ul>
  </div>
  <div class="footer-bottom">© Copyright 2018 . All Rights Reserved. Terms and Conditions | Privacy Policy</div>
</footer>

</body>
</html>
```